Lantern Software Overview Brochure

Lantern Software has developed a cloud based accounting systems for small businesses that have out grown products like Brightfern. We need an overview brochure that can be delivered in a PDF and become incorporated into our web site. I have attached our logo as a reference for colors and style.

The brochure should be speak to small business owners and communicate why Lantern is better for them than Brightfern. I will be happy to provide screen shots and content.

Target Market(s)

companies between 10 and 200 employees

Industry/Entity Type

Small Business

Requirements
Must have
• Strong branding around the Lantern name and logo. Room for screen shots of the software and discussion of product features.

```html
<!DOCTYPE html>
<html lang="en">
<head>
<meta charset="utf-8">
<title>Lantern Software Overview Brochure</title>
<link href="https://fonts.googleapis.com/css2?family=Lato:wght@300;400;700;900&display=swap" rel="stylesheet">
<style>
:root{
  --backdrop:#d9d9d9;
  --paper:#ffffff;
  --charcoal:#3a3b3d;
  --red:#c4161c;
  --ink:#222222;
  --ink-soft:#4a4a4a;
  --light-text:#e6e6e6;
  --navy:#1d2f5a;
  --blue:#3c7fd6;
  --rule:#d6dbe3;
}
*{box-sizing:border-box;margin:0;padding:0}
html,body{width:1200px;height:800px;overflow:hidden}
body{background:var(--backdrop);font-family:"Lato",Arial,sans-serif;color:var(--ink);position:relative}

.page{position:absolute;top:130px;height:540px;background:var(--paper);box-shadow:0 2px 8px rgba(0,0,0,.15);overflow:hidden}

/* inside spread */
.spread{left:20px;width:740px;display:flex}
.about{width:185px;background:var(--charcoal);color:var(--light-text);padding:34px 18px 0;position:relative}
.panel-title{font-weight:900;font-size:10px;letter-spacing:.4px;text-transform:uppercase;margin-bottom:10px}
.about .panel-title{color:#fff}
.body-copy{font-size:8.6px;line-height:1.42}
.contact-box{position:absolute;left:0;right:0;bottom:30px;background:var(--red);color:#fff;padding:14px 18px;font-size:9px;line-height:1.5}
.features{width:185px;padding:34px 18px 0;color:var(--ink)}
.features .body-copy{color:var(--ink-soft)}
.showcase{flex:1;position:relative;background:#f4f5f7}
.screens{position:absolute;left:20px;right:20px;top:22px;height:200px}
.screen{position:absolute;width:150px;height:88px;background:#fff;border:1px solid var(--rule)}
.screen-bar{height:7px;background:var(--navy)}
.screen-tabs{display:flex;gap:3px;padding:4px 5px}
.screen-tabs span{flex:1;height:6px;background:var(--blue)}
.screen-rows{padding:2px 5px}
.screen-rows span{display:block;height:2px;background:var(--rule);margin:4px 0}
.s1{left:0;top:70px}
.s2{left:170px;top:0}
.s3{left:170px;top:105px}
.photo-inside{position:absolute;left:0;right:0;bottom:0;height:300px;
  background:linear-gradient(160deg,#eef1f5 0%,#cfd8e2 45%,#9ba7b5 75%,#e7eaee 100%)}

/* front cover */
.cover{left:780px;width:400px}
.photo-cover{position:absolute;left:0;top:0;width:100%;height:290px;
  background:linear-gradient(135deg,#e9edf1 0%,#c4ccd5 50%,#8c97a4 80%,#dfe3e8 100%)}
.cover-stripe{position:absolute;left:0;top:250px;width:100%;height:60px}
.brand-name{position:absolute;left:60px;top:362px;font-weight:700;font-size:26px;color:var(--charcoal);line-height:1}
.tagline{position:absolute;left:60px;top:420px;font-size:15px;font-weight:400;color:var(--ink-soft);line-height:1.15}
</style>
</head>
<body>

<section class="page spread">
  <aside class="about">
    <h2 class="panel-title">About Us</h2>
    <p class="body-copy">Lorem ipsum dolor sit amet. In no magna commodo sea lorem. Nonumy invidunt ut consetetur deleniti at accusam. Eirmod dolores dolore. Vero erat mazim consetetur dolor soluta amet no. Nisl sanctus stet. Tempor accusam elitr vero diam. Ut ipsum veniam sanctus. Duo dolores kasd dolores cum sit. Erat ipsum aliquyam dolore. Est lorem sed aliquyam labore dolore nulla sit takimata. Nibh no diam sanctus amet eirmod. Ea sit et dolore. Invidunt iriure eos. At ex eirmod hendrerit labore tempor. Sit nobis diam accusam. Dolor ipsum wisi placerat sit justo rebum. Sadipscing et justo nihil gubergren at. Luptatum dolor. Vero ullamcorper tempor.</p>
    <div class="contact-box">
      +1 555 0134 2290<br>
      info@lanternsoftware.com<br>
      www.lanternsoftware.com
    </div>
  </aside>

  <article class="features">
    <h2 class="panel-title">Product Features</h2>
    <p class="body-copy">Lorem ipsum dolor sit amet. Gubergren tempor consectetuer invidunt no consetetur. Et magna at et iriure dolor laoreet erat. Vel diam ut erat. Stet takimata nonumy amet nonumy. Lorem diam amet cum sed gubergren facilisi. Erat accusam consequat illum no. Est at clita vel facilisi eos. Ipsum gubergren accusam ut sadipscing. No erat labore. Elit ut diam dolores et. Ea invidunt nostrud et clita et amet est. Autem dolores amet nonumy laoreet sed labore et. Exerci accusam id est. Iusto tempor lorem. Dolor esse consequat. Clita dolore clita. Dolores clita.</p>
  </article>

  <div class="showcase">
    <div class="screens">
      <div class="screen s1"><div class="screen-bar"></div><div class="screen-tabs"><span></span><span></span><span></span></div><div class="screen-rows"><span></span><span></span><span></span><span></span><span></span><span></span></div></div>
      <div class="screen s2"><div class="screen-bar"></div><div class="screen-tabs"><span></span><span></span><span></span><span></span></div><div class="screen-rows"><span></span><span></span><span></span><span></span><span></span><span></span></div></div>
      <div class="screen s3"><div class="screen-bar"></div><div class="screen-tabs"><span></span><span></span><span></span></div><div class="screen-rows"><span></span><span></span><span></span><span></span><span></span><span></span></div></div>
    </div>
    <div class="photo-inside" role="img" aria-label="Photo of a smiling businessman with colleagues meeting in a bright office"></div>
  </div>
</section>

<section class="page cover">
  <div class="photo-cover" role="img" aria-label="Photo of a business team working together in a bright office"></div>
  <svg class="cover-stripe" viewBox="0 0 400 60" preserveAspectRatio="none" aria-hidden="true">
    <polygon points="0,40 400,20 400,60 0,60" fill="#ffffff"/>
    <polygon points="0,40 400,20 400,25 0,45" fill="#c4161c"/>
  </svg>
  <h1 class="brand-name">Lantern Software</h1>
  <p class="tagline">a cloud based<br>accounting systems</p>
</section>

</body>
</html>
```